Italian / Pizza Catering Menu*

Catering Menu for Businesses .... must be clean, crispy, attractive

Want a Tri-Fold Catering Menu - See photos of Existing - see attached for content and format - but do NOT want same photos....need fresh and crisp looking foods- dislike the green

Note the front fold - it say Italian Catering

Also attached is the new Tri Fold Menu - so can get a feel for the new look

If you need high res photos, food photos, these can be uploaded - or you can use third party but must be italian food pizza related and look like our food.

Target Market(s)

Businesses to place Catering Orders

Logo Text

Fresh Catering

Logo styles of interest
Pictorial/Combination Logo
Font styles to use
Sans Serif

Requirements
Must have
• Food Photos
Pop
Fresh

Should Focus on Fast & Fresh

Also note that the catering will be offered from the following locations -

Heights 281-555-0143
3916 Copper Fen Drive, Houston, TX 77007

Brindle 713-555-0178
418 Brindle Street, Houston, TX 77002

VelT 713-555-0126
5410 Marden Parkway, #340, Houston, TX 77024

Sienna Plantation 281-555-0192
20475 Hwy 14, Ste K, Missouri City TX 77459

Pflugerville 512-555-0164
27403 Granary Business Dr #300, Pflugerville TX 78660

Delete - Franchise Opportunities information
Nice to have
• Color

```html
<!DOCTYPE html>
<html lang="en">
<head>
<meta charset="utf-8">
<title>Fresh Catering – Italian Catering Menu</title>
<link href="https://fonts.googleapis.com/css2?family=Rufina:wght@700&family=Open+Sans:wght@400;600;700&display=swap" rel="stylesheet">
<style>
:root{
  --bg:#e7e7e7;
  --black:#161616;
  --charcoal:#2d2d2d;
  --cover:#2a2a2a;
  --paper:#f4f4f4;
  --orange:#f6a623;
  --tab:#e4a94f;
  --white:#ffffff;
  --ink:#222222;
  --rule-dark:#444444;
  --rule-light:#d6d6d6;
  --badge-dark:#3a3a3a;
}
*{box-sizing:border-box;margin:0;padding:0}
html,body{width:1200px;height:591px;overflow:hidden;background:var(--bg)}
body{font-family:"Open Sans",sans-serif;position:relative}

.spread{position:absolute;top:60px;height:472px;display:flex;box-shadow:0 4px 14px rgba(0,0,0,.18)}
.spread--inside{left:10px}
.spread--outside{left:605px}
.panel{width:195px;height:100%;position:relative;overflow:hidden;padding:0 12px}
.panel--black{background:var(--black);color:var(--white)}
.panel--paper{background:var(--paper);color:var(--ink)}
.panel--charcoal{background:var(--charcoal);color:var(--white)}
.panel--cover{background:var(--cover);color:var(--white)}
.panel + .panel{border-left:1px solid rgba(0,0,0,.25)}

.photo{display:block;border-radius:2px}
.ribbon{display:block;width:max-content;margin:0 auto;background:var(--orange);color:var(--white);
  font-family:"Rufina",serif;font-weight:700;font-size:11px;line-height:1.3;padding:2px 16px;
  clip-path:polygon(0 0,100% 0,94% 50%,100% 100%,0 100%,6% 50%)}
.sub{font-size:5.6px;text-align:center;margin:5px 0 6px;opacity:.85}

.price{flex:none;width:17px;height:17px;border-radius:50%;display:flex;align-items:center;justify-content:center;
  font-family:"Rufina",serif;font-weight:700;font-size:7px;color:var(--white)}
.price--dark{background:var(--badge-dark)}
.price--orange{background:var(--orange)}
.name{font-family:"Rufina",serif;font-weight:700;font-size:9px;line-height:1.15;color:inherit}
.desc{font-size:4.6px;opacity:.8;line-height:1.35}

.row{display:flex;align-items:center;gap:5px;padding:5px 0;border-bottom:1px solid var(--rule-dark)}
.row:last-child{border-bottom:0}
.row__text{flex:1;min-width:0}
.stars{color:var(--orange);font-size:5px;letter-spacing:1px;margin-left:6px}

.grid{display:grid;grid-template-columns:1fr 1fr;column-gap:6px}
.cell{display:flex;align-items:center;gap:3px;padding:4px 0;border-bottom:1px solid var(--rule-dark)}
.panel--paper .cell{border-color:var(--rule-light)}
.cell .name{font-size:7px}
.cell .desc{font-size:4px}
.cell .price{width:14px;height:14px;font-size:6px}

.item{display:flex;justify-content:space-between;font-family:"Rufina",serif;font-weight:700;font-size:6.5px;color:var(--white)}

.table{width:100%;border-collapse:collapse;font-size:5px}
.table th{background:var(--black);color:var(--white);font-family:"Rufina",serif;font-size:7px;text-align:left;padding:2px 4px}
.table td{padding:2px 2px;border-bottom:1px solid var(--rule-light)}

.thumb{flex:none;width:20px;height:20px;border-radius:2px;background:linear-gradient(135deg,#a0603a,#d89a5e)}
.pin{flex:none;width:18px;height:18px;border-radius:50%;background:var(--orange);display:flex;align-items:center;justify-content:center}
.loc .name{font-size:7.5px}
.loc .desc{font-size:4.6px}

.pizzas{display:grid;grid-template-columns:1fr 1fr;gap:6px}
.pizza{text-align:center}
.pizza .photo{height:54px;background:radial-gradient(circle at 45% 45%,#e7a34b,#b5502c 60%,#5a3120)}
.pizza .price{margin:-9px auto 2px;position:relative}
.pizza .name{font-size:8.5px}
.pizza .desc{font-size:4.5px}
.para{font-size:5.4px;line-height:1.55;opacity:.9}

.drinks{display:flex;justify-content:space-between;margin-top:4px}
.drink{width:48px;text-align:center}
.drink .photo{width:40px;height:46px;margin:0 auto;border-radius:50%;background:radial-gradient(circle,#c9894e,#5e3a24)}
.drink .price{margin:-8px auto 2px;position:relative;width:14px;height:14px;font-size:5.5px}
.drink .name{font-size:6.5px}

.contact__title{font-family:"Rufina",serif;font-weight:700;font-size:9px;text-align:center;margin-top:12px}
.contact__addr{font-size:6.4px;text-align:center;line-height:1.5;margin-top:3px}
.contact__phone{display:flex;align-items:center;justify-content:center;gap:4px;margin-top:6px}
.contact__phone span{font-family:"Rufina",serif;font-weight:700;font-size:16px}
.contact__mail{font-size:7px;text-align:center;margin-top:3px}
.web{font-family:"Rufina",serif;font-weight:700;font-size:8.5px;text-align:center}

.cover__band{height:70px;background:var(--cover)}
.brand-tab{position:absolute;top:0;left:62px;width:106px;height:104px;background:var(--tab);display:flex;align-items:center;justify-content:center;gap:5px}
.brand-tab__mark{width:8px;height:8px;border-radius:50%;background:var(--white)}
.brand-tab__name{font-family:"Rufina",serif;font-weight:700;color:var(--white);font-size:12px;line-height:1.1}
.cover__photo{height:230px;margin:0 -12px;background:radial-gradient(ellipse at 55% 55%,#d98a3c 0%,#b24a26 40%,#6d3a22 70%,#3b2418 100%);border-bottom:2px solid var(--orange)}
.cover__title{font-family:"Rufina",serif;font-weight:700;font-size:28px;text-align:center;margin-top:24px;line-height:1}
.cover__kicker{font-family:"Rufina",serif;font-weight:700;font-size:14px;color:var(--orange);text-align:center;margin-top:5px}
.cover__sub{font-size:6.4px;text-align:center;margin-top:10px;opacity:.9}
.cover__web{position:absolute;left:0;right:0;bottom:20px}
</style>
</head>
<body>

<section class="spread spread--inside">
  <div class="panel panel--black">
    <div class="photo" role="img" aria-label="Bruschetta and antipasto platter with tomatoes and basil" style="height:98px;margin:0 -12px;background:linear-gradient(135deg,#8a5a37,#d0683e 50%,#5c3a24)"></div>
    <span class="ribbon" style="margin-top:-8px;position:relative">Antipasti</span>
    <p class="sub">Fresh starters made daily, sized for office teams.</p>
    <div class="row"><div class="row__text"><div class="name">Bruschetta Tray<span class="stars">★★★★★</span></div><div class="desc">Tomato, basil and garlic on toasted bread.</div></div><span class="price price--dark">$29</span></div>
    <div class="row"><div class="row__text"><div class="name">Garlic Knots<span class="stars">★★★★★</span></div><div class="desc">Baked fresh, butter, parsley and parmesan.</div></div><span class="price price--orange">$19</span></div>
    <div class="row"><div class="row__text"><div class="name">Caprese Platter<span class="stars">★★★★★</span></div><div class="desc">Mozzarella, tomato, basil and olive oil.</div></div><span class="price price--dark">$29</span></div>
    <div class="row"><div class="row__text"><div class="name">Meatball Tray<span class="stars">★★★★★</span></div><div class="desc">House meatballs in marinara sauce.</div></div><span class="price price--orange">$19</span></div>
    <span class="ribbon" style="margin-top:10px">Salads</span>
    <p class="sub">Crisp greens tossed to order, serves ten.</p>
    <div class="grid">
      <div class="cell"><div class="row__text"><div class="name">House Salad</div><div class="desc">Mixed greens.</div></div><span class="price price--dark">$29</span></div>
      <div class="cell"><div class="row__text"><div class="name">Caesar</div><div class="desc">Romaine, croutons.</div></div><span class="price price--dark">$49</span></div>
      <div class="cell"><div class="row__text"><div class="name">Antipasto</div><div class="desc">Salami, olives.</div></div><span class="price price--orange">$49</span></div>
      <div class="cell"><div class="row__text"><div class="name">Greek</div><div class="desc">Feta, cucumber.</div></div><span class="price price--orange">$29</span></div>
      <div class="cell"><div class="row__text"><div class="name">Caprese</div><div class="desc">Fresh mozzarella.</div></div><span class="price price--dark">$29</span></div>
      <div class="cell"><div class="row__text"><div class="name">Chef Salad</div><div class="desc">Ham, egg, cheese.</div></div><span class="price price--dark">$49</span></div>
    </div>
  </div>

  <div class="panel panel--paper">
    <span class="ribbon" style="margin-top:22px">Pasta Trays</span>
    <p class="sub">Half and full trays, served hot and ready.</p>
    <div class="grid">
      <div class="cell"><div class="row__text"><div class="name">Baked Ziti</div><div class="desc">Ricotta, marinara.</div></div><span class="price price--dark">$29</span></div>
      <div class="cell"><div class="row__text"><div class="name">Lasagna</div><div class="desc">Beef and cheese.</div></div><span class="price price--dark">$49</span></div>
      <div class="cell"><div class="row__text"><div class="name">Alfredo</div><div class="desc">Cream, parmesan.</div></div><span class="price price--orange">$49</span></div>
      <div class="cell"><div class="row__text"><div class="name">Spaghetti</div><div class="desc">With meatballs.</div></div><span class="price price--orange">$29</span></div>
      <div class="cell"><div class="row__text"><div class="name">Penne Vodka</div><div class="desc">Pink sauce.</div></div><span class="price price--dark">$29</span></div>
      <div class="cell"><div class="row__text"><div class="name">Chicken Parm</div><div class="desc">With spaghetti.</div></div><span class="price price--dark">$49</span></div>
      <div class="cell"><div class="row__text"><div class="name">Manicotti</div><div class="desc">Three cheeses.</div></div><span class="price price--orange">$49</span></div>
      <div class="cell"><div class="row__text"><div class="name">Ravioli</div><div class="desc">Cheese filled.</div></div><span class="price price--orange">$29</span></div>
    </div>
    <div style="display:flex;gap:3px;margin-top:8px">
      <div class="photo" role="img" aria-label="Bowl of spaghetti with cherry tomatoes" style="flex:1;height:48px;background:linear-gradient(135deg,#f0e6d0,#d9463a 70%,#e9d6a8)"></div>
      <div class="photo" role="img" aria-label="Baked ziti with melted cheese" style="flex:1;height:48px;background:linear-gradient(135deg,#f1e2b8,#c7683f 60%,#efe7d5)"></div>
    </div>
    <span class="ribbon" style="margin-top:10px">Pizza</span>
    <p class="sub">New York style pies, hand tossed and baked fresh.</p>
    <table class="table">
      <tr><th>Pizza Item</th><th>Large</th><th>X-Large</th></tr>
      <tr><td>Classic cheese and tomato</td><td>$29</td><td>$29</td></tr>
      <tr><td>Pepperoni and sausage</td><td>$49</td><td>$49</td></tr>
      <tr><td>Margherita with fresh basil</td><td>$29</td><td>$29</td></tr>
      <tr><td>Garden vegetable supreme</td><td>$49</td><td>$49</td></tr>
    </table>
    <div class="photo" role="img" aria-label="Sliced pepperoni pizza being served" style="position:absolute;left:0;right:0;bottom:0;height:68px;background:linear-gradient(160deg,#f2f2f2 10%,#e0a95a 40%,#c7622f 70%,#e8c07a)"></div>
  </div>

  <div class="panel panel--black">
    <span class="ribbon" style="margin-top:22px">Party Platters</span>
    <p class="sub">Boxed lunches and platters for any meeting size.</p>
    <div class="grid">
      <div class="cell"><div class="row__text"><div class="item"><span>Italian Sub</span><span>$29</span></div><div class="desc">Salami, ham, provolone</div></div></div>
      <div class="cell"><div class="row__text"><div class="item"><span>Wing Tray</span><span>$39</span></div><div class="desc">Buffalo or garlic parm</div></div></div>
      <div class="cell"><div class="row__text"><div class="item"><span>Stromboli</span><span>$29</span></div><div class="desc">Sliced for sharing</div></div></div>
      <div class="cell"><div class="row__text"><div class="item"><span>Calzones</span><span>$39</span></div><div class="desc">Ricotta and mozzarella</div></div></div>
      <div class="cell"><div class="row__text"><div class="item"><span>Box Lunch</span><span>$29</span></div><div class="desc">Sub, salad and cookie</div></div></div>
      <div class="cell"><div class="row__text"><div class="item"><span>Cannoli</span><span>$39</span></div><div class="desc">One dozen, filled fresh</div></div></div>
    </div>
    <span class="ribbon" style="margin-top:16px">Hot Subs</span>
    <p class="sub">Toasted on fresh-baked Italian bread.</p>
    <div class="row"><div class="photo" role="img" aria-label="Meatball sub" style="width:30px;height:24px;background:linear-gradient(#e2b36a,#9a3e26 60%,#c99a55)"></div><div class="row__text"><div class="name">Meatball Sub</div><div class="desc">Meatballs, marinara and melted<br>provolone on a toasted roll.</div></div><span class="price price--dark">$29</span></div>
    <div class="row"><div class="photo" role="img" aria-label="Chicken parmesan sub" style="width:30px;height:24px;background:linear-gradient(#e2b36a,#b0582c 60%,#c99a55)"></div><div class="row__text"><div class="name">Chicken Parm</div><div class="desc">Breaded chicken, marinara and<br>mozzarella on a toasted roll.</div></div><span class="price price--orange">$29</span></div>
    <div class="row"><div class="photo" role="img" aria-label="Sausage and peppers sub" style="width:30px;height:24px;background:linear-gradient(#e2b36a,#8a4a2a 60%,#c99a55)"></div><div class="row__text"><div class="name">Sausage &amp; Peppers</div><div class="desc">Italian sausage, peppers and<br>onions on a toasted roll.</div></div><span class="price price--dark">$29</span></div>
    <div class="row"><div class="photo" role="img" aria-label="Eggplant parmesan sub" style="width:30px;height:24px;background:linear-gradient(#e2b36a,#7a4a2a 60%,#c99a55)"></div><div class="row__text"><div class="name">Eggplant Parm</div><div class="desc">Breaded eggplant, marinara and<br>mozzarella on a toasted roll.</div></div><span class="price price--orange">$29</span></div>
  </div>
</section>

<section class="spread spread--outside">
  <div class="panel panel--charcoal">
    <span class="ribbon" style="margin-top:22px">Catering Locations</span>
    <p class="sub">Order from the location nearest your business.</p>
    <div class="row loc"><span class="pin"><svg width="9" height="9" viewBox="0 0 24 24" aria-hidden="true"><path fill="#fff" d="M12 2a7 7 0 0 0-7 7c0 5 7 13 7 13s7-8 7-13a7 7 0 0 0-7-7zm0 9.5A2.5 2.5 0 1 1 12 6.5a2.5 2.5 0 0 1 0 5z"/></svg></span><div class="row__text"><div class="name">Heights · 281-555-0143</div><div class="desc">3916 Copper Fen Drive, Houston, TX 77007</div></div></div>
    <div class="row loc"><span class="pin"><svg width="9" height="9" viewBox="0 0 24 24" aria-hidden="true"><path fill="#fff" d="M12 2a7 7 0 0 0-7 7c0 5 7 13 7 13s7-8 7-13a7 7 0 0 0-7-7zm0 9.5A2.5 2.5 0 1 1 12 6.5a2.5 2.5 0 0 1 0 5z"/></svg></span><div class="row__text"><div class="name">Brindle · 713-555-0178</div><div class="desc">418 Brindle Street, Houston, TX 77002</div></div></div>
    <div class="row loc"><span class="pin"><svg width="9" height="9" viewBox="0 0 24 24" aria-hidden="true"><path fill="#fff" d="M12 2a7 7 0 0 0-7 7c0 5 7 13 7 13s7-8 7-13a7 7 0 0 0-7-7zm0 9.5A2.5 2.5 0 1 1 12 6.5a2.5 2.5 0 0 1 0 5z"/></svg></span><div class="row__text"><div class="name">VelT · 713-555-0126</div><div class="desc">5410 Marden Parkway, #340, Houston, TX 77024</div></div></div>
    <div class="row loc"><span class="pin"><svg width="9" height="9" viewBox="0 0 24 24" aria-hidden="true"><path fill="#fff" d="M12 2a7 7 0 0 0-7 7c0 5 7 13 7 13s7-8 7-13a7 7 0 0 0-7-7zm0 9.5A2.5 2.5 0 1 1 12 6.5a2.5 2.5 0 0 1 0 5z"/></svg></span><div class="row__text"><div class="name">Sienna Plantation · 281-555-0192</div><div class="desc">20475 Hwy 14, Ste K, Missouri City TX 77459</div></div></div>
    <div class="row loc"><span class="pin"><svg width="9" height="9" viewBox="0 0 24 24" aria-hidden="true"><path fill="#fff" d="M12 2a7 7 0 0 0-7 7c0 5 7 13 7 13s7-8 7-13a7 7 0 0 0-7-7zm0 9.5A2.5 2.5 0 1 1 12 6.5a2.5 2.5 0 0 1 0 5z"/></svg></span><div class="row__text"><div class="name">Pflugerville · 512-555-0164</div><div class="desc">27403 Granary Business Dr #300, Pflugerville TX 78660</div></div></div>
    <p class="para" style="margin-top:6px">Please place catering orders 24 hours ahead. Delivery, setup, plates and utensils are available for every order.</p>
    <span class="ribbon" style="margin-top:14px">Drinks &amp; Desserts</span>
    <p class="sub">Round out the meal for your team.</p>
    <div class="drinks">
      <div class="drink"><div class="photo" role="img" aria-label="Iced tea pitcher"></div><span class="price price--orange">$19</span><div class="name">Iced Tea</div><div class="desc">Gallon, sweet or plain</div></div>
      <div class="drink"><div class="photo" role="img" aria-label="Cannoli on a plate"></div><span class="price price--orange">$19</span><div class="name">Cannoli</div><div class="desc">One dozen</div></div>
      <div class="drink"><div class="photo" role="img" aria-label="Tiramisu slices"></div><span class="price price--orange">$19</span><div class="name">Tiramisu</div><div class="desc">Tray of twelve</div></div>
    </div>
  </div>

  <div class="panel panel--charcoal">
    <span class="ribbon" style="margin-top:22px">Pizza Party</span>
    <p class="sub">Hot, fresh pies delivered to your office.</p>
    <div class="pizzas">
      <div class="pizza"><div class="photo" role="img" aria-label="Pepperoni pizza with peppers"></div><span class="price price--orange">$29</span><div class="name">Pepperoni</div><div class="desc">Mozzarella and pepperoni</div></div>
      <div class="pizza"><div class="photo" role="img" aria-label="Cheese pizza with olives"></div><span class="price price--orange">$29</span><div class="name">Margherita</div><div class="desc">Tomato, basil, mozzarella</div></div>
      <div class="pizza"><div class="photo" role="img" aria-label="Sliced vegetable pizza"></div><span class="price price--orange">$29</span><div class="name">Veggie</div><div class="desc">Peppers, onions, mushroom</div></div>
      <div class="pizza"><div class="photo" role="img" aria-label="Salami pizza"></div><span class="price price--orange">$29</span><div class="name">Meat Lovers</div><div class="desc">Sausage, salami, bacon</div></div>
    </div>
    <span class="ribbon" style="margin-top:12px">Fast &amp; Fresh</span>
    <p class="para" style="margin-top:8px">Every order is made fresh the day you need it, with crisp vegetables, hand-stretched dough and sauces cooked in house. We deliver on time so your meeting starts on schedule.</p>
    <div class="contact__title">Catering Orders</div>
    <p class="contact__addr">Five locations in Houston,<br>Missouri City and Pflugerville.</p>
    <div class="contact__phone">
      <svg width="11" height="11" viewBox="0 0 24 24" aria-hidden="true"><path fill="#f6a623" d="M6.6 10.8a15.1 15.1 0 0 0 6.6 6.6l2.2-2.2a1 1 0 0 1 1-.25 11.4 11.4 0 0 0 3.6.57 1 1 0 0 1 1 1V20a1 1 0 0 1-1 1A17 17 0 0 1 3 4a1 1 0 0 1 1-1h3.5a1 1 0 0 1 1 1c0 1.25.2 2.45.57 3.57a1 1 0 0 1-.25 1z"/></svg>
      <span>281-555-0143</span>
    </div>
    <p class="contact__mail">Email: orders@freshcateringtx.com</p>
    <p class="web" style="margin-top:12px">www.freshcateringtx.com</p>
  </div>

  <div class="panel panel--cover">
    <div class="cover__band"></div>
    <div class="cover__photo" role="img" aria-label="Close-up of a fresh pizza with salami, olives and basil on a wooden board"></div>
    <div class="brand-tab"><span class="brand-tab__mark"></span><span class="brand-tab__name">Fresh<br>Catering</span></div>
    <h1 class="cover__title">Italian Catering</h1>
    <p class="cover__kicker">Fast &amp; Fresh</p>
    <p class="cover__sub">Pizza, pasta and platters for your business.</p>
    <p class="web cover__web">www.freshcateringtx.com</p>
  </div>
</section>

</body>
</html>
```